Manifesto

I want a manifesto with the following five manifestos for our Not for Profit

- We are a For-purpose organisation
- Every service we offer is free
- Every product we sell funds our services
- Every financial transaction is transparent
- Our service is for the greater good
- Our purpose is always to serve the people
- We are a for purpose organisation

Its to go with this website logo/look/feel www.brightlantern.co.nz

Two attachments:

1. I quite like this look/feel of a manifesto (see attached), I want something clean, professional but I also quite like either Retro modern look feel also like a fresh, and uplifting as its for sick people coming to see us and our funds where anyone buys a product are used for helping those who are sick with healing......so needs something conveyed that is fresh, uplifing yet professional.
2. This attachment is how I wrote this down when inspired of how I wanted Bright Lantern to operate. This is our values chart. It has to say

Also check out our website for our logo, look etc.. it doesnt have to be the same but red somewhere would link back to logo. www.brightlantern.co.nz .

```html
<!DOCTYPE html>
<html lang="en">
<head>
<meta charset="utf-8">
<title>Bright Lantern – Our Manifesto</title>
<link rel="stylesheet" href="https://fonts.googleapis.com/css2?family=Arimo:wght@400;700&family=Nothing+You+Could+Do&display=swap">
<style>
  :root {
    --ink-grey: #58595b;
    --script-grey: #8c8c8c;
    --brand-red: #b8202e;
    --paper: #ffffff;
    --sans: "Arimo", Arial, sans-serif;
    --script: "Nothing You Could Do", cursive;
  }
  * { margin: 0; padding: 0; box-sizing: border-box; }
  html, body { width: 927px; height: 1200px; overflow: hidden; background: var(--paper); }
  .manifesto {
    position: relative;
    width: 927px;
    height: 1200px;
    background: var(--paper);
    font-family: var(--sans);
    color: var(--ink-grey);
  }
  .brand {
    position: absolute;
    top: 94px;
    left: 0;
    width: 100%;
    text-align: center;
  }
  .brand-name {
    display: inline-flex;
    align-items: center;
    gap: 10px;
    font-family: var(--sans);
    font-weight: 700;
    font-size: 32px;
    color: var(--brand-red);
    line-height: 1;
  }
  .brand-dot {
    width: 20px;
    height: 20px;
    border-radius: 50%;
    background: var(--brand-red);
  }
  .title {
    position: absolute;
    top: 210px;
    left: 0;
    width: 100%;
    text-align: center;
    font-family: var(--script);
    font-weight: 400;
    font-size: 118px;
    line-height: 1;
    color: var(--script-grey);
  }
  .pledge {
    position: absolute;
    left: 0;
    width: 927px;
    text-align: center;
    line-height: 1;
    font-weight: 700;
    white-space: nowrap;
  }
  .accent { color: var(--brand-red); }
  .pledge--purpose      { top: 392px; font-size: 38.5px; }
  .pledge--free         { top: 458px; font-size: 44px; }
  .pledge--product      { top: 544px; font-size: 60px; font-weight: 400; }
  .pledge--funds        { top: 604px; font-size: 70px; color: var(--brand-red); }
  .pledge--transparent  { top: 698px; font-size: 31px; }
  .pledge--service      { top: 768px; font-size: 76px; }
  .pledge--good         { top: 832px; font-size: 77px; color: var(--brand-red); }
  .pledge--people       { top: 946px; font-size: 32px; }
  .pledge--spaced {
    top: 1020px;
    left: 66px;
    width: 810px;
    font-size: 46px;
    display: flex;
    justify-content: space-between;
  }
  .pledge--organisation { top: 1078px; font-size: 62.5px; color: var(--brand-red); }
</style>
</head>
<body>
<main class="manifesto">
  <header class="brand">
    <div class="brand-name"><span class="brand-dot"></span>Bright Lantern</div>
  </header>

  <h1 class="title">Our Manifesto</h1>

  <p class="pledge pledge--purpose">WE ARE A <span class="accent">FOR-PURPOSE</span> ORGANISATION</p>
  <p class="pledge pledge--free">EVERY SERVICE WE OFFER IS <span class="accent">FREE</span></p>
  <p class="pledge pledge--product">EVERY PRODUCT WE SELL</p>
  <p class="pledge pledge--funds">FUNDS OUR SERVICES</p>
  <p class="pledge pledge--transparent">EVERY FINANCIAL TRANSACTION IS <span class="accent">TRANSPARENT</span></p>
  <p class="pledge pledge--service">OUR SERVICE IS FOR</p>
  <p class="pledge pledge--good">THE GREATER GOOD</p>
  <p class="pledge pledge--people">OUR PURPOSE IS ALWAYS TO <span class="accent">SERVE THE PEOPLE</span></p>
  <p class="pledge pledge--spaced" aria-label="We are a for">
    <span>W</span><span>E</span><span>&nbsp;</span><span>A</span><span>R</span><span>E</span><span>&nbsp;</span><span>A</span><span>&nbsp;</span><span>F</span><span>O</span><span>R</span>
  </p>
  <p class="pledge pledge--organisation">PURPOSE ORGANISATION</p>
</main>
</body>
</html>
```